A brand new wordpress website for my business which will replace my current site www.harbornetcall.com.au, As i rank quite well in google will it be ok to keep my current URL's. I sell the following service and products

1. Voip Provider (Main service) we sell directly the the end user but also we would like to get resellers and agents to sell our services. agents selling our brand resellers sell our services branded as theirs
2. Hosted Pbx (main service) home page must push this service explaining the benifits and features that come with a hosted pbx, we also have business plans based on number of extensions (phones) the customer requires
3. Tornax IP Pbx (product) only selling IP Pbx and selected software
4. Velbox IP Pbx (product)
5. Quorvin IP Phones (this is the main VoIP phone we sell)
6. lumora phones (to be on a landing page only not apart of the main site)
7. selected headsets from Dravensonic (products)
8. Meridal Conference phone (VoIP model only)
9. we can supply fax to email service

we would like a support page with user guides (step by step instructions on our products and services and FAQ's about all products and services

we have a carrier grade softswitch (telco billing system) z7ledger http://www.pinwheelledger.org this system has a ticketing system, customer and agent login I would like a URL link from our website so customers can login to this system. also it is possible to skin z7ledger to look like our website

VoIP business plans

$0 per month
call rate .12c land line calls
.24c per minute mobile calls

$25 per month
250 Free local land line calls
call rate is .10c land line calls .22c per minute mobile calls

$50 per month
500 Free local land line calls
call rate .09 land line calls .20c per minute mobile calls

$100 per month
1000 free local land line calls
call rate .08c land line calls .18c per minute mobile calls

all mobile calls are billed per second no flag fall

also require a link to international call rates

We can port your existing telephone number from any carrier or supply new Australian telephone numbers

02, 03, 07, 08, 131, 1300, 1800

Designs i like www.tralcom.com.au and www.orbitelphone.com

I would like the website to be white and bright

Reason: Please use images of the products I sell only

Target Market(s)

business customers only

Industry/Entity Type

Requirements
Must have
• all pages must have its own banner to reflect the product or service we are selling. the home page can automatically change to show all pages with a link straight to the page in question

for example if on the home page the banner for quorvin phone is displaying if someone click on the banner they will be redirected to the quorvin page

Must Be SEO friendly
Nice to have
• shopping cart via paypal for all products but before customer checks out i would like to offer two options

1. Pre configure the item and ship to your address for existing customers
2. would you like a harbor net call technician to attend your office and install the item in person (costs involved $60 call out fee $120 per hours every item sold charge .50 hour and only the one call out fee)

new and existing customers can book service work via the website
1. describe the work required (maybe we need to give a few option)
2. company details
3. pre payment (checkout via paypal) can we put the paypal fees back on to the customer?

```html
<!DOCTYPE html>
<html lang="en">
<head>
<meta charset="utf-8">
<title>Harbor Net Call – Business VoIP &amp; Hosted PBX</title>
<link rel="stylesheet" href="https://fonts.googleapis.com/css2?family=Dosis:wght@300;400;500&family=Open+Sans:wght@400;600;700&display=swap">
<style>
:root{
  --sky:#a9cfee;
  --sky-deep:#8fbde6;
  --brand-blue:#1e5fa8;
  --ink:#333333;
  --muted:#666666;
  --line:#dddddd;
  --nav-grey:#e6e6e6;
  --nav-active:#d6d6d6;
  --footer:#a8a8a8;
  --white:#ffffff;
  --orange:#f58220;
  --page:#ffffff;
}
*{box-sizing:border-box;margin:0;padding:0}
html,body{width:1200px;height:2313px;overflow:hidden;background:var(--page)}
body{position:relative;font-family:"Open Sans",Arial,sans-serif;color:var(--ink)}
.abs{position:absolute}
ul{list-style:none}

/* top bar */
.top-rule{left:0;top:0;width:1200px;height:6px;background:var(--sky)}
.login-tab{left:662px;top:0;width:118px;height:42px;background:var(--sky);color:var(--white);font:600 17px "Open Sans",sans-serif;text-align:center;line-height:44px;border-radius:0 0 8px 8px}
.social-top{left:1015px;top:16px;display:flex;gap:12px}
.social-top span{width:32px;height:32px;border-radius:50%;background:var(--sky-deep)}

/* brand */
.brand{left:100px;top:58px;display:flex;align-items:center;gap:14px}
.brand-mark{width:22px;height:22px;border-radius:50%;background:var(--brand-blue)}
.brand-name{font:500 44px/1 "Dosis",sans-serif;color:var(--brand-blue);letter-spacing:1px}
.util-nav{right:31px;top:72px;display:flex;gap:16px;font:600 15px "Open Sans",sans-serif;color:var(--ink)}
.contact-line{right:31px;top:112px;font:400 13px "Open Sans",sans-serif;color:var(--ink);display:flex;gap:18px}

/* main nav */
.main-nav{left:470px;top:152px;width:699px;height:57px;background:var(--nav-grey);display:flex;align-items:center;justify-content:space-between;font:600 17px "Open Sans",sans-serif;color:var(--ink)}
.main-nav li{padding:0 24px;height:57px;line-height:57px;white-space:nowrap}
.main-nav li.active{background:var(--nav-active)}

/* hero */
.hero{left:100px;top:211px;width:1069px;height:390px;background:var(--white);box-shadow:0 14px 18px -10px rgba(0,0,0,.35);overflow:hidden;border:1px solid var(--line)}
.hero-title{left:24px;top:30px;width:340px;font:500 30px/1.25 "Open Sans",sans-serif;color:var(--brand-blue)}
.hero-copy{left:24px;top:116px;width:340px;font:400 16px/1.45 "Open Sans",sans-serif;color:var(--muted)}
.hero-product{left:40px;top:232px;width:290px;height:140px;border-radius:44% 44% 40% 40%;background:radial-gradient(ellipse at 50% 45%,#6b6b6b,#222 70%)}
.hero-photo{left:516px;top:0;width:553px;height:390px;background:linear-gradient(120deg,#d9d2cc 0%,#c9a48a 40%,#e6ddd4 100%)}
.slider-arrows{left:40px;top:208px;width:38px;height:126px;border:1px solid var(--line);background:var(--white)}
.slider-arrows svg{display:block}

/* dropdown */
.dropdown{left:470px;top:209px;width:228px;background:var(--nav-grey);padding:6px 0;box-shadow:0 4px 8px rgba(0,0,0,.2)}
.dropdown li{font:400 13px/36px "Open Sans",sans-serif;color:var(--ink);padding-left:30px;border-bottom:1px solid #cfcfcf;white-space:nowrap}
.dropdown li:last-child{border-bottom:0}

/* live support */
.live-support{left:1141px;top:612px;width:47px;height:160px;background:var(--orange);border-radius:6px 0 0 6px;color:var(--white);font:700 15px "Open Sans",sans-serif;display:flex;align-items:center;justify-content:center}
.live-support span{transform:rotate(-90deg);white-space:nowrap}

/* section heads */
.section-head{left:100px;width:1069px;text-align:center;font:300 52px/1 "Dosis",sans-serif;color:var(--ink);letter-spacing:1px}
.section-head::after{content:"";display:block;margin:18px auto 0;width:1069px;height:1px;background:var(--line)}

/* plans */
.plans{left:100px;top:797px;width:1069px;height:324px;background:var(--sky);display:flex}
.plan{flex:1;display:flex;flex-direction:column;align-items:center;color:var(--white);text-align:center}
.plan-badge{margin-top:32px;width:116px;height:116px;border-radius:50%;background:var(--white);color:var(--sky-deep);display:flex;flex-direction:column;align-items:center;justify-content:center}
.plan-badge small{font:600 10px "Open Sans",sans-serif;letter-spacing:.5px}
.plan-badge strong{font:400 48px/1 "Dosis",sans-serif}
.plan h3{margin-top:24px;font:600 17px "Open Sans",sans-serif}
.plan p{font:600 13px/26px "Open Sans",sans-serif}
.plan h3+p{margin-top:10px}

/* billing banner */
.billing-banner{left:100px;top:1149px;width:1069px;height:136px;background:linear-gradient(#f4f4f4,#e3e3e3);border:1px solid var(--line);display:flex;align-items:center}
.billing-brand{margin-left:6px;width:340px;height:104px;background:var(--white);display:flex;align-items:center;gap:16px;padding-left:22px}
.billing-brand i{width:44px;height:44px;background:var(--brand-blue)}
.billing-brand b{font:500 48px "Dosis",sans-serif;color:var(--brand-blue)}
.billing-tag{margin-left:48px;font:400 44px/1.1 "Dosis",sans-serif;color:#444;letter-spacing:1px;white-space:nowrap}
.billing-shot{position:absolute;right:0;top:0;width:300px;height:134px;background:linear-gradient(135deg,#ffffff,#cfd8e3)}

/* service */
.service-intro{left:100px;top:1470px;width:510px}
.service-intro h2{font:400 29px/1.4 "Open Sans",sans-serif;color:var(--ink)}
.service-intro .lead{margin-top:34px;font:400 19px/1.5 "Open Sans",sans-serif;color:var(--muted)}
.benefits{margin-top:26px}
.benefits li{display:flex;align-items:center;gap:12px;font:400 15.5px/38px "Open Sans",sans-serif;color:var(--ink);white-space:nowrap}
.benefits svg{flex:none}

.feature-card{left:635px;top:1467px;width:534px;height:208px;border:1px solid var(--line);background:var(--white);overflow:hidden}
.feature-card h3{position:absolute;left:18px;top:18px;font:600 17px "Open Sans",sans-serif;color:var(--ink);white-space:nowrap}
.feature-card p{position:absolute;left:18px;top:58px;width:250px;font:400 16px/1.4 "Open Sans",sans-serif;color:var(--ink)}
.feature-photo{position:absolute;right:0;top:0;width:240px;height:208px;background:linear-gradient(150deg,#f1e0d3,#caa48c 60%,#3c3c3c)}

.stories{left:635px;top:1700px;width:534px}
.stories h3{font:600 19px "Open Sans",sans-serif;color:var(--ink)}
.stories blockquote{position:relative;margin-top:22px;padding:0 40px 0 34px;font:400 15px/2 "Open Sans",sans-serif;color:var(--muted)}
.stories svg{position:absolute}

/* footer */
.footer{left:0;top:1933px;width:1200px;height:380px;background:var(--footer)}
.footer-col{top:1950px}
.footer-col h4{font:500 23px "Dosis",sans-serif;color:var(--white);letter-spacing:.5px}
.footer-col ul{margin-top:14px}
.footer-col li{font:600 12.5px/31px "Open Sans",sans-serif;color:var(--white);white-space:nowrap}
.footer-col li::before{content:"› ";}
.footer-bottom{left:0;top:2242px;width:1200px;display:flex;justify-content:center;align-items:center;gap:10px;font:600 12px "Open Sans",sans-serif;color:var(--white)}
.footer-bottom i{width:28px;height:28px;border-radius:50%;background:var(--white)}
</style>
</head>
<body>

<div class="abs top-rule"></div>
<div class="abs login-tab">LOGIN</div>
<div class="abs social-top"><span></span><span></span></div>

<div class="abs brand"><span class="brand-mark"></span><span class="brand-name">Harbor Net Call</span></div>
<ul class="abs util-nav"><li>HOME</li><li>ABOUT</li><li>CONTACT</li></ul>
<div class="abs contact-line"><span>Tel: +1 300 482 917</span><span>Email: hello@harbornetcall.example</span></div>

<section class="abs hero">
  <h1 class="abs hero-title">CONTRARY TO POPULAR BELIEF</h1>
  <p class="abs hero-copy">Established fact that a reader will be distracted by the readable content of a page when looking at its layout.</p>
  <div class="abs hero-product" role="img" aria-label="Conference phone product photo"></div>
  <div class="abs hero-photo" role="img" aria-label="Photo of a support agent wearing a headset"></div>
</section>
<div class="abs slider-arrows">
  <svg width="36" height="124" viewBox="0 0 36 124"><path d="M21 22l-8 9 8 9" fill="none" stroke="#888" stroke-width="2"/><line x1="0" y1="62" x2="36" y2="62" stroke="#ddd"/><path d="M21 84l-8 9 8 9" fill="none" stroke="#888" stroke-width="2"/></svg>
</div>

<ul class="abs main-nav">
  <li class="active">PRODUCTS</li><li>HOSTED PBX</li><li>TELEPHONE SYSTEMS</li><li>PLANS &amp; SIGNUP</li>
</ul>
<ul class="abs dropdown">
  <li>IP Telephones</li><li>Conference Phone</li><li>Headsets</li><li>Routers &amp; Modems</li><li>Velbox IP Telephone System</li><li>Tornax Quadro</li><li>Dect Phones</li>
</ul>

<div class="abs live-support"><span>LIVE SUPPORT</span></div>

<h2 class="abs section-head" style="top:724px">VOIP BUSINESS PLANS</h2>

<section class="abs plans">
  <div class="plan"><div class="plan-badge"><small>PER MONTH</small><strong>$0</strong></div><h3>CALL RATE</h3><p>.12c land line calls</p><p>.24c per minute mobile calls</p></div>
  <div class="plan"><div class="plan-badge"><small>PER MONTH</small><strong>$25</strong></div><h3>CALL RATE</h3><p>.10c land line calls</p><p>.22c per minute mobile calls</p><p>250 Free local land line calls</p></div>
  <div class="plan"><div class="plan-badge"><small>PER MONTH</small><strong>$50</strong></div><h3>CALL RATE</h3><p>.09c land line calls</p><p>.20c per minute mobile calls</p><p>500 Free local land line calls</p></div>
  <div class="plan"><div class="plan-badge"><small>PER MONTH</small><strong>$100</strong></div><h3>CALL RATE</h3><p>.08c land line calls</p><p>.18c per minute mobile calls</p><p>1000 Free local land line calls</p></div>
</section>

<section class="abs billing-banner">
  <div class="billing-brand"><i></i><b>z7ledger</b></div>
  <p class="billing-tag">SAY NO TO HUGE<br>LINE RENTAL</p>
  <div class="billing-shot" role="img" aria-label="Screenshot of the billing system dashboard"></div>
</section>

<h2 class="abs section-head" style="top:1378px">WHICH SERVICE IS RIGHT FOR ME?</h2>

<section class="abs service-intro">
  <h2>Small to Medium Business Phone Systems &amp; Hosted PBX Solutions</h2>
  <p class="lead">Harbor Net Call can get you started with a feature rich and low upfront cost VoIP Phone System.</p>
  <ul class="benefits">
    <li><svg width="18" height="18" viewBox="0 0 18 18"><rect x="1" y="1" width="16" height="16" fill="none" stroke="#333" stroke-width="1.5"/><path d="M4 9l4 4 8-10" fill="none" stroke="#333" stroke-width="2"/></svg>Low upfront phone system costs to get started - from $0.09c</li>
    <li><svg width="18" height="18" viewBox="0 0 18 18"><rect x="1" y="1" width="16" height="16" fill="none" stroke="#333" stroke-width="1.5"/><path d="M4 9l4 4 8-10" fill="none" stroke="#333" stroke-width="2"/></svg>Self manage your VoIP phone system via friendly web interface</li>
    <li><svg width="18" height="18" viewBox="0 0 18 18"><rect x="1" y="1" width="16" height="16" fill="none" stroke="#333" stroke-width="1.5"/><path d="M4 9l4 4 8-10" fill="none" stroke="#333" stroke-width="2"/></svg>Novaphone/laptop phone system integration</li>
    <li><svg width="18" height="18" viewBox="0 0 18 18"><rect x="1" y="1" width="16" height="16" fill="none" stroke="#333" stroke-width="1.5"/><path d="M4 9l4 4 8-10" fill="none" stroke="#333" stroke-width="2"/></svg>No on site technician charges</li>
    <li><svg width="18" height="18" viewBox="0 0 18 18"><rect x="1" y="1" width="16" height="16" fill="none" stroke="#333" stroke-width="1.5"/><path d="M4 9l4 4 8-10" fill="none" stroke="#333" stroke-width="2"/></svg>Always be up to date with phone system technology</li>
    <li><svg width="18" height="18" viewBox="0 0 18 18"><rect x="1" y="1" width="16" height="16" fill="none" stroke="#333" stroke-width="1.5"/><path d="M4 9l4 4 8-10" fill="none" stroke="#333" stroke-width="2"/></svg>Link multiple office/home together as one</li>
  </ul>
</section>

<aside class="abs feature-card">
  <h3>NOVAPHONE INTEGRATION</h3>
  <p>Connect your Novaphone with your IP desk phone. Never miss calls when you leave the office.</p>
  <div class="feature-photo" role="img" aria-label="Hand holding a smartphone"></div>
</aside>

<aside class="abs stories">
  <h3>CUSTOMER STORIES</h3>
  <blockquote>
    <svg style="left:0;top:6px" width="20" height="14" viewBox="0 0 20 14"><path d="M2 14V8l4-8h3L6 7h3v7zM11 14V8l4-8h3l-3 7h3v7z" fill="#999"/></svg>
    There are many variations of passages of Lorem Ipsum available, but the majority have suffered alteration in some form, by injected humour, or randomised words which don't look even slightly believable.
    <svg style="right:6px;bottom:4px" width="20" height="14" viewBox="0 0 20 14"><path d="M18 0v6l-4 8h-3l3-7h-3V0zM9 0v6l-4 8H2l3-7H2V0z" fill="#999"/></svg>
  </blockquote>
</aside>

<footer>
  <div class="abs footer"></div>
  <nav class="abs footer-col" style="left:100px"><h4>ABOUT</h4><ul><li>ABOUT HARBOR NET CALL</li><li>WHY HNC HOSTED PBX</li><li>DECT PHONE</li></ul></nav>
  <nav class="abs footer-col" style="left:350px"><h4>PRODUCTS</h4><ul><li>IP TELEPHONES</li><li>CONFERENCE PHONE</li><li>HEADSETS</li><li>ROUTERS &amp; MODEMS</li><li>VELBOX IP TELEPHONE SYSTEM</li><li>TORNAX QUADRO</li><li>DECT PHONES</li></ul></nav>
  <nav class="abs footer-col" style="left:591px"><h4>PLANS &amp; SIGNUP</h4><ul><li>PLANS</li><li>SIGNUP</li></ul></nav>
  <nav class="abs footer-col" style="left:833px"><h4>OTHERS</h4><ul><li>HOME</li><li>HOSTED PBX</li><li>CONTACT</li><li>TELEPHONE SYSTEMS</li><li>TERMS AND PRIVACY</li><li>RETURNS POLICY</li><li>SITEMAP</li></ul></nav>
  <div class="abs footer-bottom"><i></i><i></i><span>Copyright © 2013 Harbor Net Call</span></div>
</footer>

</body>
</html>
```